Casa Bellorno Togo Menu seperated in categories

new to go menu for italian restaurant with menu descriptions and prices i like the cover first page to have all the restaurant information, the other pages should be separated in the menu categories, and if we can include a map with the location of the restaurant
Casa Bellorno
42 Route 58 S
North Myrtle Beach, SC 29617
open 7 days a week 4-10
Happy hour served Daily at the Bar 4-7
www.casabellorno.com
casabellornomb@mailbox.example

Industry/Entity Type

Restaurant

Font styles to use
Sans Serif

Requirements
Must have
• Prices and pictures and restaurant information

```html
<!DOCTYPE html>
<html lang="en">
<head>
<meta charset="utf-8">
<title>Casa Bellorno – Seafood</title>
<link rel="stylesheet" href="https://fonts.googleapis.com/css2?family=Questrial&display=swap">
<style>
  :root {
    --backdrop: #c98b5e;
    --panel: #f2f3f5;
    --green: #3a8371;
    --red: #b5144a;
    --white: #ffffff;
    --ink: #111111;
  }
  html, body {
    margin: 0;
    padding: 0;
    width: 849px;
    height: 1200px;
    overflow: hidden;
    background: var(--backdrop);
  }
  .canvas {
    position: relative;
    width: 827px;
    height: 1169px;
    transform: scale(1.02660);
    transform-origin: 0 0;
    font-family: "Questrial", "Century Gothic", sans-serif;
  }
  .border-art {
    position: absolute;
    inset: 0;
  }
  .menu-panel {
    position: absolute;
    left: 103px;
    top: 95px;
    width: 619px;
    height: 980px;
    background: var(--panel);
  }
  .section-title {
    position: absolute;
    left: 118px;
    top: 115px;
    margin: 0;
    font-size: 19px;
    font-weight: 700;
    color: var(--green);
    letter-spacing: 0.3px;
  }
  .section-intro {
    position: absolute;
    left: 118px;
    top: 138px;
    width: 591px;
    margin: 0;
    font-size: 15.6px;
    line-height: 21.2px;
    color: var(--green);
    text-align: justify;
    hyphens: auto;
  }
  .dish {
    position: absolute;
    left: 118px;
    width: 591px;
    line-height: 20.8px;
  }
  .dish-name {
    margin: 0;
    font-size: 17px;
    font-weight: 400;
    color: var(--red);
  }
  .dish-desc {
    margin: 0;
    font-size: 15px;
    color: var(--ink);
    text-align: justify;
    hyphens: auto;
  }
  .dish-price {
    margin: 0;
    font-size: 15px;
    color: var(--ink);
  }
  .dish-photo {
    position: absolute;
    left: 0;
    top: 0;
  }
</style>
</head>
<body>
<div class="canvas">
  <svg class="border-art" width="827" height="1169" viewBox="0 0 827 1169" aria-hidden="true">
    <defs>
      <pattern id="pills-top" patternUnits="userSpaceOnUse" x="103" y="45" width="103.17" height="120">
        <rect x="0.7" y="0" width="33" height="120" rx="16.5" fill="var(--green)"/>
        <rect x="35.1" y="0" width="33" height="120" rx="16.5" fill="var(--white)"/>
        <rect x="69.5" y="0" width="33" height="120" rx="16.5" fill="var(--red)"/>
      </pattern>
      <pattern id="pills-bottom" patternUnits="userSpaceOnUse" x="103" y="1005" width="103.17" height="120">
        <rect x="0.7" y="0" width="33" height="120" rx="16.5" fill="var(--green)"/>
        <rect x="35.1" y="0" width="33" height="120" rx="16.5" fill="var(--white)"/>
        <rect x="69.5" y="0" width="33" height="120" rx="16.5" fill="var(--red)"/>
      </pattern>
      <pattern id="pills-left" patternUnits="userSpaceOnUse" x="57" y="95" width="120" height="105">
        <rect x="0" y="0.8" width="120" height="33.4" rx="16.7" fill="var(--red)"/>
        <rect x="0" y="35.8" width="120" height="33.4" rx="16.7" fill="var(--white)"/>
        <rect x="0" y="70.8" width="120" height="33.4" rx="16.7" fill="var(--green)"/>
      </pattern>
      <pattern id="pills-right" patternUnits="userSpaceOnUse" x="650" y="95" width="120" height="105">
        <rect x="0" y="0.8" width="120" height="33.4" rx="16.7" fill="var(--green)"/>
        <rect x="0" y="35.8" width="120" height="33.4" rx="16.7" fill="var(--white)"/>
        <rect x="0" y="70.8" width="120" height="33.4" rx="16.7" fill="var(--red)"/>
      </pattern>
      <radialGradient id="plate-tones" cx="0.5" cy="0.48" r="0.55">
        <stop offset="0" stop-color="#d77a3c"/>
        <stop offset="0.35" stop-color="#e7b25a"/>
        <stop offset="0.62" stop-color="#e9ecef"/>
        <stop offset="1" stop-color="#c9d0d8"/>
      </radialGradient>
    </defs>
    <rect x="103" y="45" width="619" height="110" fill="url(#pills-top)"/>
    <rect x="103" y="1005" width="619" height="120" fill="url(#pills-bottom)"/>
    <rect x="57" y="95" width="120" height="980" fill="url(#pills-left)"/>
    <rect x="650" y="95" width="120" height="980" fill="url(#pills-right)"/>
  </svg>

  <div class="menu-panel"></div>

  <h1 class="section-title">SEAFOOD</h1>
  <p class="section-intro">All of our Seafood Dishes served with fresh baked bread and our roasted red pepper, garlic and herb dipping oil, your choice of soup of the day or house salad, upgrade to Caesar Salad 1.95. Split Entrée includes additional soup or salad 7.00</p>

  <div class="dish" style="top:260px">
    <h2 class="dish-name">Linguini With Clams Sauce</h2>
    <p class="dish-desc">Fresh little neck Clams sautéed in extra virgin oil, Garlic chunks and baby Clams in their own juice, served over linguini in a Red or White sauce</p>
    <p class="dish-price">18.95</p>
  </div>

  <div class="dish" style="top:363px">
    <h2 class="dish-name">Spaghetti With Mussels</h2>
    <p class="dish-desc">Fresh PEI Mussels sautéed with your choice of Marinara, Scampi or Fra Diavolo sauce, served over spaghetti</p>
    <p class="dish-price">18.95</p>
  </div>

  <div class="dish" style="top:467px">
    <h2 class="dish-name">Shrimp &amp; Scallops</h2>
    <p class="dish-desc">Choice of Shrimp or fresh Sea Scallops or Combo, sautéed in your choice of Marinara, Scampi or Fra Diavolo sauce, served over linguini</p>
    <p class="dish-price">24.95</p>
  </div>

  <div class="dish" style="top:570px">
    <h2 class="dish-name">Grouper Florentine</h2>
    <p class="dish-desc">Fresh Grouper egg battered, finished in a lemon chardonnay butter sauce, and served over spinach and linguini</p>
    <p class="dish-price">25.95</p>
  </div>

  <div class="dish" style="top:673px">
    <h2 class="dish-name">Zuppa Di Pesce</h2>
    <p class="dish-desc">Shrimp, Sea Scallops, Calamari, PEI Mussels, Little Neck Clams and Grouper, sautéed in your choice of Marinara or Fra Diavolo sauce, served over linguini</p>
    <p class="dish-price">28.95</p>
  </div>

  <svg class="dish-photo" width="827" height="1169" viewBox="0 0 827 1169">
    <ellipse cx="433" cy="912" rx="200" ry="143" fill="var(--red)"/>
    <ellipse cx="431" cy="904" rx="191" ry="128" fill="url(#plate-tones)" role="img" aria-label="Photo of penne with grouper and mussels in a tomato cream sauce on a white plate"/>
  </svg>
</div>
</body>
</html>
```